Law Firm Business Card

This is a business card for a law firm that serves US military and veterans.

The card must have ONLY the following (we want an uncluttered look):

- Company logo (PNG, GIF, JPEG copies uploaded)
- A tagline reading: "a law firm for service members and veterans"
- My name and title: "Martin Okello" and "Attorney"
- My email: "martin.okello@harborlinecounsel.com"
- My number: "855-FILE-NOW (345-3669)"

We are looking for a clean, simple layout with only the above information, likely printed on a bright white cotton stock. The font of our logo is DIN 1451, and the font used on our website is Helvetica Neue. The color of our logo is #336699, and we probably want the tagline in that color also, and my contact information in a dark grey. Please review our website at www.harborlinecounsel.com to ensure your card design complements our website style.

Thanks and we look forward to seeing your submissions.

A few notes:

- Two-sided submissions are ok
- Please don't add graphics (scales of justice, judges hammer, etc)

```html
<!DOCTYPE html>
<html lang="en">
<head>
<meta charset="utf-8">
<title>Harborline Counsel — Business Card</title>
<link rel="stylesheet" href="https://fonts.googleapis.com/css2?family=Montserrat:wght@500;700&family=Questrial&display=swap">
<style>
  :root {
    --page: #ffffff;
    --card: #f2f4ea;
    --frame: #4f5557;
    --brand-blue: #2a5db5;
    --band-blue: #b8cadf;
    --edge-blue: #1f5fc4;
    --ink-grey: #4d5356;
    --tag-text: #f4f4f4;
    --mark-soft: #d9dfe3;
  }
  html, body {
    margin: 0;
    padding: 0;
    width: 1200px;
    height: 700px;
    overflow: hidden;
    background: var(--page);
  }
  .card {
    position: absolute;
    left: 43px;
    top: 43px;
    width: 1116px;
    height: 604px;
    background: var(--card);
    border: 3px solid var(--frame);
    overflow: hidden;
  }
  .brand-name {
    position: absolute;
    left: 50px;
    top: 40px;
    width: 400px;
    margin: 0;
    font-family: "Montserrat", sans-serif;
    font-weight: 700;
    font-size: 46px;
    line-height: 1.05;
    letter-spacing: 1px;
    color: var(--brand-blue);
    text-align: center;
    text-transform: uppercase;
  }
  .brand-emblem {
    position: absolute;
    left: 845px;
    top: 27px;
    width: 232px;
    height: 160px;
    border-radius: 6px;
    background: linear-gradient(90deg, var(--ink-grey) 0%, var(--ink-grey) 50%, var(--brand-blue) 50%, var(--brand-blue) 100%);
    opacity: 0.85;
  }
  .tagline {
    position: absolute;
    left: 0;
    top: 170px;
    width: 557px;
    height: 36px;
    background: var(--ink-grey);
    color: var(--tag-text);
    font-family: "Montserrat", sans-serif;
    font-weight: 500;
    font-size: 16px;
    line-height: 36px;
    padding-left: 18px;
    box-sizing: border-box;
    text-decoration: underline;
    letter-spacing: 0.4px;
    margin: 0;
  }
  .person {
    position: absolute;
    left: 442px;
    top: 240px;
    margin: 0;
  }
  .person-name {
    margin: 0;
    font-family: "Montserrat", sans-serif;
    font-weight: 700;
    font-size: 40px;
    letter-spacing: 3px;
    color: var(--ink-grey);
  }
  .person-title {
    margin: 6px 0 0 210px;
    font-family: "Questrial", sans-serif;
    font-size: 31px;
    letter-spacing: 3px;
    color: var(--ink-grey);
  }
  .contact-band {
    position: absolute;
    left: 0;
    top: 442px;
    width: 1058px;
    height: 148px;
    background: var(--band-blue);
  }
  .contact-edge {
    position: absolute;
    left: 1068px;
    top: 442px;
    width: 48px;
    height: 148px;
    background: var(--edge-blue);
  }
  .contact-line {
    position: absolute;
    margin: 0;
    font-family: "Questrial", sans-serif;
    color: var(--ink-grey);
    letter-spacing: 2px;
    white-space: nowrap;
  }
  .contact-label {
    color: var(--brand-blue);
    font-weight: 700;
    font-family: "Montserrat", sans-serif;
  }
  .contact-email {
    left: 52px;
    top: 468px;
    font-size: 25px;
  }
  .contact-email .contact-label { margin-right: 18px; }
  .contact-phone {
    left: 40px;
    top: 522px;
    font-size: 29px;
  }
  .contact-phone .contact-label { margin-right: 10px; }
</style>
</head>
<body>
  <main class="card">
    <h1 class="brand-name">Harborline<br>Counsel</h1>
    <div class="brand-emblem" role="img" aria-label="Firm emblem area"></div>

    <p class="tagline">a law firm for service members and veterans</p>

    <section class="person">
      <h2 class="person-name">Martin Okello</h2>
      <p class="person-title">Attorney</p>
    </section>

    <div class="contact-band"></div>
    <div class="contact-edge"></div>
    <p class="contact-line contact-email"><span class="contact-label">@:</span>martin.okello@harborlinecounsel.com</p>
    <p class="contact-line contact-phone"><span class="contact-label">Ph:</span>855-FILE-NOW (345-3669)</p>
  </main>
</body>
</html>
```